Business Card Project for Firm Deck Hoisting

Business name is "Firm Deck Hoisting" we are a scaffolding & rigging business specialising in local and remote work for:
- scaffolding (residential, commercial, industrial)
- rigging
-man material hoists
- swing stages
- labour hire

On the back of the card I would like FDH as the symbol / logo. I have attached the logos we have had created by sketch harbour. We would like to use bold colours – preferably as the same colour scheme as the logo.

Target Market(s)

Construction business

Industry/Entity Type

Construction

Contact Information for Business Card

name: Owen Pellew
Title: Director
Phone: 0491 572 864
Address: PO BOX 3251, Kestrel Vale SA 5190
Email: owen@firmdeckhoisting.com.au
Website: www.firmdeckhoisting.com.au

Font styles to use
Sans Serif

Requirements
Must have
• Must use existing logo & prefering using bold colours
Nice to have
• Would be nice to have a line of dot points in what we specialise in but not essential
• Would be nice to see some designs with a slogan but not essential
Should not have
• NA

```html
<!DOCTYPE html>
<html lang="en">
<head>
<meta charset="utf-8">
<title>Firm Deck Hoisting – Business Card</title>
<link rel="stylesheet" href="https://fonts.googleapis.com/css2?family=Montserrat:wght@400;500;700;800&display=swap">
<style>
  :root {
    --backdrop: #2a2a2c;
    --card: #ffffff;
    --ink: #2a2a2c;
    --ink-soft: #4a4a4e;
    --brand-blue: #2f7fc1;
  }
  * { margin: 0; padding: 0; box-sizing: border-box; }
  html, body {
    width: 1200px;
    height: 900px;
    overflow: hidden;
    background: var(--backdrop);
    font-family: "Montserrat", sans-serif;
    color: var(--ink);
  }
  .card {
    position: absolute;
    width: 620px;
    height: 380px;
    background: var(--card);
    border-radius: 22px;
    box-shadow: 0 18px 40px rgba(0,0,0,0.45);
  }
  /* Logo side */
  .card--brand { left: 90px; top: 60px; }
  .brand-lockup {
    position: absolute;
    left: 0; right: 0; top: 140px;
    display: flex;
    align-items: center;
    justify-content: center;
    gap: 14px;
  }
  .brand-dot {
    width: 22px; height: 22px;
    border-radius: 50%;
    background: var(--brand-blue);
  }
  .brand-name {
    font-weight: 800;
    font-size: 34px;
    letter-spacing: 0.5px;
    color: var(--ink);
    text-transform: uppercase;
  }
  .brand-web {
    position: absolute;
    left: 0; right: 0; top: 262px;
    display: flex;
    justify-content: center;
    align-items: center;
    gap: 8px;
    font-size: 15px;
    color: var(--ink);
  }
  .brand-web .domain { color: var(--brand-blue); }

  /* Contact side */
  .card--contact { left: 490px; top: 460px; }
  .monogram {
    position: absolute;
    right: 48px; top: 56px;
    font-weight: 800;
    font-size: 96px;
    line-height: 1;
    letter-spacing: 4px;
    color: var(--ink);
  }
  .postal {
    position: absolute;
    right: 48px; top: 178px;
    text-align: right;
    font-size: 15px;
    line-height: 1.45;
    color: var(--ink-soft);
  }
  .person {
    position: absolute;
    left: 44px; top: 200px;
  }
  .person-name {
    font-weight: 700;
    font-size: 20px;
    color: var(--brand-blue);
    text-transform: uppercase;
    letter-spacing: 0.3px;
  }
  .person-title {
    font-size: 14px;
    margin-top: 4px;
    color: var(--ink-soft);
  }
  .contact-list {
    position: absolute;
    left: 44px; top: 268px;
    list-style: none;
    font-size: 15px;
    color: var(--ink);
  }
  .contact-list li {
    display: flex;
    align-items: center;
    gap: 12px;
    height: 26px;
  }
  .contact-list .domain { color: var(--brand-blue); }
  .icon { width: 15px; height: 15px; flex: none; }
</style>
</head>
<body>

<section class="card card--brand" aria-label="Card front">
  <div class="brand-lockup">
    <span class="brand-dot"></span>
    <span class="brand-name">Firm Deck Hoisting</span>
  </div>
  <p class="brand-web">
    <svg class="icon" viewBox="0 0 16 16" aria-hidden="true">
      <circle cx="8" cy="8" r="7" fill="var(--brand-blue)"/>
      <g fill="none" stroke="#fff" stroke-width="1">
        <ellipse cx="8" cy="8" rx="3" ry="6.2"/>
        <line x1="1.5" y1="8" x2="14.5" y2="8"/>
      </g>
    </svg>
    <span>www.<span class="domain">firmdeckhoisting</span>.com.au</span>
  </p>
</section>

<section class="card card--contact" aria-label="Card back">
  <div class="monogram">FDH</div>
  <p class="postal">PO BOX 3251,<br>Kestrel Vale SA 5190</p>

  <div class="person">
    <h1 class="person-name">Owen Pellew</h1>
    <p class="person-title">Director</p>
  </div>

  <ul class="contact-list">
    <li>
      <svg class="icon" viewBox="0 0 16 16" aria-hidden="true">
        <path d="M2 6c0-2 2-3 6-3s6 1 6 3v1h-3V5.5H5V7H2z" fill="var(--brand-blue)"/>
        <rect x="3.5" y="8" width="9" height="6" rx="1.2" fill="var(--brand-blue)"/>
        <circle cx="8" cy="11" r="1.5" fill="#fff"/>
      </svg>
      <span>0491 572 864</span>
    </li>
    <li>
      <svg class="icon" viewBox="0 0 16 16" aria-hidden="true">
        <path d="M15 1 1 7l6 2 2 6z" fill="var(--brand-blue)"/>
      </svg>
      <span>owen@firmdeckhoisting.com.au</span>
    </li>
    <li>
      <svg class="icon" viewBox="0 0 16 16" aria-hidden="true">
        <circle cx="8" cy="8" r="7" fill="var(--brand-blue)"/>
        <g fill="none" stroke="#fff" stroke-width="1">
          <ellipse cx="8" cy="8" rx="3" ry="6.2"/>
          <line x1="1.5" y1="8" x2="14.5" y2="8"/>
        </g>
      </svg>
      <span>www.<span class="domain">firmdeckhoisting.com.au</span></span>
    </li>
  </ul>
</section>

</body>
</html>
```